fresh noodle packaging

we need to rebrand our existing brand which base for asia market in australia, we need a fresher look which market for more western style.

i attached our existing product, involved two logo, we want to make all design into one brand only, ( Bao Tin instead of noodle quillon)

requirement:
trendy
fresh
economical
" looks" enviromental friendly
cost effective

one design as a signature and represent the company, expect to fit all type of noodle except text and color
Updates

Need extra days to review

Target Market(s)

supermarket e.g vantrel

Requirements
Must have
• remain color from our old packaging

```html
<!DOCTYPE html>
<html lang="en">
<head>
<meta charset="utf-8">
<title>Bao Tin Hokkien Noodle – Packaging Samples</title>
<link rel="stylesheet" href="https://fonts.googleapis.com/css2?family=Lobster&family=Open+Sans:wght@600&family=Roboto+Slab:wght@400;700&display=swap">
<style>
  :root {
    --navy: #141a66;
    --red: #c8070f;
    --white: #ffffff;
    --paper: #f7f7f8;
    --board-light: #f3f3f4;
    --board-dark: #d9d9db;
    --label: #4a4a4c;
  }
  * { margin: 0; padding: 0; box-sizing: border-box; }
  html, body { width: 1200px; height: 848px; overflow: hidden; }
  body {
    position: relative;
    background: radial-gradient(ellipse at 50% 45%, var(--board-light) 0%, var(--board-dark) 100%);
    font-family: "Roboto Slab", Georgia, serif;
  }
  .label-card { position: absolute; }
  .label-card--one { left: 79px; top: 90px; width: 497px; height: 660px; }
  .label-card--two { left: 630px; top: 95px; width: 488px; height: 650px; }
  .label-card > svg.card-shape { position: absolute; inset: 0; }
  .abs { position: absolute; white-space: nowrap; line-height: 1; }

  .brand-mark { display: flex; align-items: center; gap: 6px; }
  .brand-mark__dot { width: 16px; height: 16px; border-radius: 50%; background: var(--red); }
  .brand-mark__name { font-weight: 700; font-size: 17px; color: var(--navy); }

  .brand-title { font-family: "Lobster", cursive; color: var(--red); font-size: 124px; }
  .brand-sub { font-family: "Lobster", cursive; color: var(--navy); font-size: 44px; }
  .brand-title--outlined, .brand-sub--outlined {
    text-shadow:
      2px 0 0 var(--white), -2px 0 0 var(--white), 0 2px 0 var(--white), 0 -2px 0 var(--white),
      2px 2px 0 var(--white), -2px -2px 0 var(--white), 2px -2px 0 var(--white), -2px 2px 0 var(--white);
  }
  .product-name { font-family: "Lobster", cursive; font-size: 70px; }
  .product-name--navy { color: var(--navy); }
  .product-name--red { color: var(--red); }

  .illustration-slot {
    position: absolute;
    border-radius: 40% 40% 30% 30%;
    background: radial-gradient(ellipse at 55% 45%, rgba(200,7,15,0.22) 0%, rgba(200,7,15,0.08) 60%, rgba(200,7,15,0) 75%);
  }

  .info { font-weight: 400; }
  .info--navy { color: var(--navy); }
  .info--white { color: var(--white); }
  .info--red { color: var(--red); }
  .info--small { font-size: 12.5px; line-height: 15px; }
  .info--code { font-size: 10px; line-height: 11.5px; }
  .right { text-align: right; }
  .net { font-weight: 700; font-size: 19px; color: var(--white); }
  .promo { font-weight: 400; font-size: 20px; line-height: 22px; color: var(--red); }
  .maker { font-weight: 700; font-size: 17px; color: var(--white); letter-spacing: 0.5px; }
  .address { font-size: 10px; color: var(--white); }
  .no-pres { font-weight: 700; font-size: 11px; color: var(--white); }
  .no-pres--vertical { font-size: 17px; transform: rotate(-90deg); transform-origin: left top; }

  .badge-slot { position: absolute; border-radius: 50%; }
  .badge-slot--light { border: 2px solid var(--white); }
  .badge-slot--red { border: 2px solid var(--red); }
  .origin-slot { position: absolute; border: 2px solid var(--white); border-radius: 2px; }

  .sample-caption {
    position: absolute; top: 792px; width: 200px; text-align: center;
    font-family: "Open Sans", Arial, sans-serif; font-weight: 600; font-size: 22px; color: var(--label);
  }
</style>
</head>
<body>

<!-- Sample 1 -->
<section class="label-card label-card--one">
  <svg class="card-shape" width="497" height="660" viewBox="0 0 497 660">
    <defs>
      <clipPath id="card-one-clip"><rect x="0" y="0" width="497" height="660" rx="32"/></clipPath>
    </defs>
    <rect x="0" y="0" width="497" height="660" rx="32" fill="var(--navy)"/>
    <g clip-path="url(#card-one-clip)">
      <rect x="6" y="6" width="485" height="648" rx="27" fill="var(--paper)"/>
      <path d="M0,385 Q180,610 497,515" fill="none" stroke="var(--red)" stroke-width="5"/>
      <path d="M0,402 Q180,625 497,527 L497,660 L0,660 Z" fill="var(--navy)"/>
    </g>
  </svg>

  <div class="abs brand-mark" style="left:30px; top:80px;">
    <span class="brand-mark__dot"></span><span class="brand-mark__name">Bao Tin</span>
  </div>
  <div class="abs brand-title" style="left:160px; top:2px;">Brand</div>
  <div class="abs brand-sub" style="left:258px; top:110px;">Name Here</div>

  <div class="illustration-slot" role="img" aria-label="Line illustration of a smiling chef giving an OK hand sign" style="left:185px; top:225px; width:305px; height:312px;"></div>

  <div class="abs product-name product-name--navy" style="left:33px; top:228px;">Hokkien</div>
  <div class="abs product-name product-name--red" style="left:68px; top:286px;">Noodle</div>
  <svg class="abs" style="left:108px; top:350px;" width="175" height="20" viewBox="0 0 175 20">
    <path d="M2,18 Q85,0 173,8" fill="none" stroke="var(--red)" stroke-width="4" stroke-linecap="round"/>
  </svg>

  <div class="badge-slot badge-slot--light" role="img" aria-label="Halal certification badge" style="left:24px; top:505px; width:62px; height:62px;"></div>
  <div class="abs info info--white info--small" style="left:24px; top:592px;">LOREM IPSUM SIMPLY<br>DUMMY TEXT</div>
  <div class="abs info info--red info--code" style="left:24px; top:628px;">ABC-XXX-XXX-XX<br>EFG-XXX-XXX-XX</div>

  <div class="abs no-pres" style="left:197px; top:600px;">No Preservatives</div>
  <div class="origin-slot" role="img" aria-label="Country of origin badge" style="left:195px; top:616px; width:103px; height:31px;"></div>

  <div class="abs net right" style="right:11px; top:547px;">Net : 2 kg</div>
  <div class="abs promo right" style="right:11px; top:570px;">LOREM IPSUM<br>DUMMY TEXT</div>
  <div class="abs maker right" style="right:11px; top:622px;">BAO TIN FOOD MFR</div>
  <div class="abs address right" style="right:20px; top:644px;">Your Company Address Goes Here</div>
</section>

<!-- Sample 2 -->
<section class="label-card label-card--two">
  <svg class="card-shape" width="488" height="650" viewBox="0 0 488 650">
    <defs>
      <clipPath id="card-two-clip"><rect x="0" y="0" width="488" height="650" rx="32"/></clipPath>
    </defs>
    <rect x="0" y="0" width="488" height="650" rx="32" fill="var(--navy)"/>
    <g clip-path="url(#card-two-clip)">
      <rect x="6" y="6" width="476" height="638" rx="27" fill="var(--paper)"/>
      <path d="M298,0 L366,109 C425,230 440,420 385,515 C320,610 200,635 90,660 L488,660 L488,0 Z" fill="var(--navy)"/>
      <path d="M372,160 C418,270 420,430 365,515 C300,600 170,638 40,660" fill="none" stroke="var(--red)" stroke-width="5"/>
    </g>
  </svg>

  <div class="abs brand-mark" style="left:28px; top:82px;">
    <span class="brand-mark__dot"></span><span class="brand-mark__name">Bao Tin</span>
  </div>
  <div class="abs brand-title brand-title--outlined" style="left:152px; top:6px;">Brand</div>
  <div class="abs brand-sub brand-sub--outlined" style="left:250px; top:108px;">Name Here</div>

  <div class="illustration-slot" role="img" aria-label="Line illustration of a smiling chef giving an OK hand sign" style="left:112px; top:182px; width:152px; height:141px;"></div>

  <div class="abs product-name product-name--navy" style="left:62px; top:316px;">Hokkien</div>
  <div class="abs product-name product-name--red" style="left:96px; top:372px;">Noodle</div>
  <svg class="abs" style="left:142px; top:438px;" width="182" height="20" viewBox="0 0 182 20">
    <path d="M2,18 Q90,0 180,10" fill="none" stroke="var(--red)" stroke-width="4" stroke-linecap="round"/>
  </svg>

  <div class="abs no-pres no-pres--vertical" style="left:448px; top:362px; font-size:19px;">No Preservatives</div>
  <div class="origin-slot" role="img" aria-label="Country of origin badge" style="left:434px; top:380px; width:41px; height:136px;"></div>

  <div class="badge-slot badge-slot--red" role="img" aria-label="Halal certification badge" style="left:22px; top:490px; width:60px; height:60px;"></div>
  <div class="abs info info--navy info--small" style="left:23px; top:582px;">LOREM IPSUM SIMPLY<br>DUMMY TEXT</div>
  <div class="abs info info--red info--code" style="left:22px; top:617px;">ABC-XXX-XXX-XX<br>EFG-XXX-XXX-XX</div>

  <div class="abs net right" style="right:10px; top:533px;">Net : 2 kg</div>
  <div class="abs promo right" style="right:10px; top:556px;">LOREM IPSUM<br>DUMMY TEXT</div>
  <div class="abs maker right" style="right:10px; top:608px;">BAO TIN FOOD MFR</div>
  <div class="abs address right" style="right:20px; top:630px;">Your Company Address Goes Here</div>
</section>

<div class="sample-caption" style="left:228px;">SAMPLE 1</div>
<div class="sample-caption" style="left:774px;">SAMPLE 2</div>

</body>
</html>
```